Personal Training Business at home (Fern Wellness & Health)

My business name will be Fern Wellness & Health and will be training people with special needs (Asthma, Diabetes, Obesity, Rehab, Sports Performance) for all ages. It will be set indoor and outdoor for all types of weather conditions. I,m also doing Pilates group classes as well in a Japanese garden setting.I will be working alone so the groups will be small and the client has a high quality of service. I just need something very basic to start with then as the business expands I can edit it to it,s growth.

Target Market(s)

Target special population persons with dysfunctions injuries, metabolic/cardio-respiratory conditions, sports performance and more also healthy food choices.

Industry/Entity Type

Business

Number of Pages Required

3 page

Font styles to use
Serif

Colors
f78f20
ffffff
474747
cbcbcb
abd036

Requirements
Must have
• The website must have accessibility for change, to be able to link on other networks like my own YouTube videos. A basic lay out so I can fill in the pages and ad more as I expand the business. The logo to have the A for Arch to be an image of a man shaped as the letter A with his arms extended out/up. Private Facility and must ring for appointment to enter premises.
Nice to have
• The Image I want to have in my studio is for people to be serious about training & health choices. I want them to be able to train in a comfortable environment and free of air conditioned concrete rooms with machines. My home is converted to a Organic feature and outdoor/indoor training facility that my clients & I can share the natural freedom of training in the elements. My client have special needs and need extra care, they are people with injuries, metabolic/cardio-respiratory condition, asthmatics & more they need to be screened and tested for the condition that they suffer from and together with there allied professional we work together to treat them with the up most care for maximum results. This is what I want to target I long term client with real Goals on there mind and not some pipe dream.
Should not have
• Not to be portray as a Gym with machines and clients that only care about image.

```html
<!DOCTYPE html>
<html lang="en">
<head>
<meta charset="utf-8">
<title>Fern Wellness &amp; Health</title>
<link rel="stylesheet" href="https://fonts.googleapis.com/css2?family=Cinzel:wght@400;600&family=Montserrat:wght@300;400;600;700&family=Open+Sans:wght@300;400;600;700&family=PT+Serif:wght@700&display=swap">
<style>
:root{
  --leaf:#abd036;
  --leaf-deep:#93b82a;
  --amber:#f78f20;
  --ink:#474747;
  --stone:#cbcbcb;
  --white:#ffffff;
  --mist:#ebebeb;
  --charcoal:#363636;
  --night:#222222;
  --serif:'Cinzel', Georgia, serif;
  --sans:'Open Sans', Arial, sans-serif;
  --display:'Montserrat', Arial, sans-serif;
}
*{box-sizing:border-box;margin:0;padding:0}
html,body{width:1200px;height:3135px;overflow:hidden}
body{position:relative;background:var(--white);font-family:var(--sans);color:var(--ink)}
.abs{position:absolute}

/* header */
.site-header{position:absolute;left:0;top:0;width:1200px;height:127px;background:var(--white)}
.brand{position:absolute;left:100px;top:22px;display:flex;align-items:center;gap:14px}
.brand-dot{width:58px;height:58px;border-radius:50%;background:var(--leaf);flex:none}
.brand-name{font-family:var(--serif);font-weight:600;color:var(--leaf);font-size:27px;line-height:1.05;width:230px}
.utility{position:absolute;top:22px;right:60px;display:flex;align-items:center;gap:18px;font-size:10px;color:var(--ink)}
.client-login{background:var(--leaf);color:var(--white);font-weight:700;font-size:9px;padding:3px 8px;letter-spacing:.3px}
.util-item{display:flex;align-items:center;gap:5px}
.util-item b{color:var(--amber);font-weight:600}
.call{line-height:1.2;text-align:left}
.main-nav{position:absolute;left:514px;top:42px;height:81px;display:flex;font-family:var(--display);font-size:22px}
.main-nav a{display:flex;align-items:center;justify-content:center;padding:0 12px;color:#222;text-decoration:none;position:relative}
.main-nav a+a::before{content:"";position:absolute;left:0;top:28px;height:28px;border-left:1px solid var(--stone)}
.main-nav a.is-active{background:var(--leaf);color:var(--white);width:97px;padding:0}
.main-nav a.is-active+a::before{display:none}

/* hero */
.hero{position:absolute;left:4px;top:127px;width:1192px;height:511px;overflow:hidden}
.hero-photo{position:absolute;inset:0;background:
  radial-gradient(ellipse at 78% 10%, #f7e7a6 0%, rgba(247,231,166,0) 40%),
  linear-gradient(180deg,#7f8b3a 0%,#a7953f 35%,#8a7a4d 62%,#b9aa8c 80%,#9d917b 100%)}
.hero-arrow{position:absolute;top:200px;width:40px;height:80px}
.appointment{position:absolute;left:161px;top:36px;width:311px;height:443px;background:var(--leaf);padding-top:20px}
.appointment h2{font-family:var(--display);font-weight:400;color:var(--white);font-size:26px;text-align:center;line-height:34px}
.field{position:absolute;left:22px;width:267px;height:34px;display:flex;align-items:center}
.field svg{width:20px;height:20px;flex:none}
.field span{margin-left:21px;width:226px;height:34px;background:var(--white);font-size:11px;color:#9a9a9a;display:flex;align-items:center;padding-left:10px;position:relative}
.field .caret{position:absolute;right:0;top:0;width:26px;height:34px;background:#e2e2e2;display:flex;align-items:center;justify-content:center}
.submit-row{position:absolute;left:0;top:363px;width:311px;height:40px;display:flex;align-items:center;justify-content:center;gap:16px}
.submit-btn{width:193px;height:40px;background:var(--white);color:#bdbdbd;font-family:var(--display);font-size:18px;letter-spacing:1px;display:flex;align-items:center;justify-content:center}
.appointment-note{position:absolute;left:20px;top:418px;width:271px;text-align:center;color:var(--white);font-weight:700;font-size:12.5px;line-height:18px}

/* welcome */
.welcome-title{position:absolute;right:682px;top:742px;text-align:right;font-family:var(--display);font-weight:400;color:var(--leaf);font-size:45px;line-height:56px}
.welcome-rule{position:absolute;left:541px;top:713px;height:192px;border-left:1px solid var(--stone)}
.welcome-body{position:absolute;left:554px;top:718px;width:460px}
.welcome-body h3{font-family:var(--serif);font-weight:400;color:var(--leaf);font-size:30px;line-height:36px;margin-bottom:8px}
.welcome-body p{font-size:13.5px;line-height:17.5px;color:#555}
.btn{display:inline-flex;align-items:center;justify-content:center;background:var(--amber);color:var(--white);font-weight:700;font-family:var(--sans)}
.welcome-body .btn{width:110px;height:34px;font-size:13px;margin-top:10px}

/* expertise */
.expertise{position:absolute;left:0;top:968px;width:1200px;height:562px;background:var(--mist)}
.section-title{position:absolute;left:0;width:1200px;text-align:center;font-family:var(--display);font-weight:400;font-size:30px}
.section-title strong{font-weight:600}
.tile{position:absolute;width:273px;height:183px;overflow:hidden}
.tile .photo{position:absolute;inset:0}
.tile .label{position:absolute;left:10px;bottom:10px;color:var(--white);font-family:var(--display);font-weight:600;font-size:17px;text-shadow:0 1px 2px rgba(0,0,0,.35)}
.tile .band{position:absolute;left:0;right:0;bottom:0;height:38px;background:rgba(171,208,54,.45)}
.tile-more .plus{position:absolute;left:80px;top:35px;width:112px;height:112px;border-radius:50%;background:rgba(255,255,255,.25);display:flex;align-items:center;justify-content:center}

/* about */
.about-photo{position:absolute;left:165px;top:1622px;width:231px;height:106px}
.about-text{position:absolute;left:438px;top:1618px;width:595px;font-size:11.5px;line-height:14.6px;color:#3f3f3f}
.about-text p+p{margin-top:9px}
.thumb{position:absolute;top:1906px;width:130px;height:74px}

/* news & blog */
.updates{position:absolute;left:0;top:2022px;width:1200px;height:467px;background:var(--mist)}
.col-title{position:absolute;font-family:var(--display);font-weight:400;color:var(--leaf);font-size:30px}
.col-title strong{font-weight:700}
.news-photo{position:absolute;left:163px;top:2144px;width:341px;height:169px}
.news-rule{position:absolute;left:163px;top:2318px;width:341px;border-top:2px solid #9a9a9a}
.news-text{position:absolute;left:165px;top:2324px;width:340px;font-size:10px;line-height:16px;color:#333}
.small-btn{position:absolute;width:89px;height:25px;font-size:9px}
.updates-rule{position:absolute;left:586px;top:2113px;height:340px;border-left:1px solid var(--stone)}
.post-thumb{position:absolute;left:675px;width:80px;height:74px}
.post{position:absolute;left:768px;width:260px;font-size:9.5px;line-height:13.5px;color:#333}
.post time{display:block;font-weight:700;font-size:10px;margin-bottom:3px}
.read-more{position:absolute;right:0;font-weight:700;font-size:10px}

/* testimonials */
.testimonials-title{position:absolute;left:0;top:2530px;width:1200px;text-align:center;font-family:var(--display);color:var(--amber);font-size:33px;font-weight:400}
.testimonials-sub{position:absolute;left:0;top:2575px;width:1200px;text-align:center;font-size:13px;color:#333}
.quote{position:absolute;top:2618px;width:336px;height:107px;background:var(--mist);padding:14px 16px 0 20px;font-size:8.5px;line-height:12.5px;color:#555}
.quote::before{content:"\201C";position:absolute;left:10px;top:5px;font-size:14px;color:#777}
.quote::after{content:"";position:absolute;left:26px;bottom:-10px;border-left:10px solid transparent;border-right:10px solid transparent;border-top:10px solid var(--mist)}
.avatar{position:absolute;top:2747px;width:51px;height:54px}
.person{position:absolute;top:2755px;font-family:'PT Serif', Georgia, serif;font-weight:700;font-size:16px;color:#222}
.person small{display:block;font-family:var(--sans);font-weight:400;font-size:8px;color:#888}
.t-arrow{position:absolute;top:2648px;width:24px;height:44px}

/* footer */
.site-footer{position:absolute;left:0;top:2852px;width:1200px;height:245px;background:var(--charcoal);color:var(--white)}
.foot-title{position:absolute;top:59px;font-weight:700;font-size:13px;letter-spacing:.5px}
.quick-links{position:absolute;left:38px;top:95px;list-style:none;font-size:13.5px;line-height:18px}
.contact-info{position:absolute;left:338px;top:88px;font-size:14.5px;line-height:19px}
.contact-info .pin{position:absolute;left:-26px;top:2px}
.contact-info .lines{margin-top:18px}
.foot-input{position:absolute;height:36px;background:var(--white);color:#333;font-size:11px;display:flex;align-items:center;justify-content:center}
.foot-submit{position:absolute;left:628px;top:178px;width:216px;height:32px;background:var(--leaf);color:var(--white);font-size:10px;font-weight:700;display:flex;align-items:center;justify-content:center}
.foot-brand{position:absolute;left:958px;top:80px;display:flex;align-items:center;gap:10px}
.foot-brand .brand-dot{width:40px;height:40px}
.foot-brand .brand-name{font-size:20px;width:150px}
.social{position:absolute;left:1005px;top:172px;display:flex;gap:8px}
.social span{width:18px;height:18px;border-radius:50%;background:var(--white)}
.copyright{position:absolute;left:0;top:3097px;width:1200px;height:38px;background:var(--night);color:var(--white);font-size:9px;font-weight:700;padding:14px 0 0 38px}
</style>
</head>
<body>

<header class="site-header">
  <div class="brand">
    <span class="brand-dot"></span>
    <span class="brand-name">Fern Wellness &amp; Health</span>
  </div>
  <div class="utility">
    <span class="client-login">CLIENT LOGIN</span>
    <span class="util-item">
      <svg width="18" height="13" viewBox="0 0 18 13"><rect x="0" y="0" width="18" height="13" fill="#f78f20"/><path d="M0 0 L9 7 L18 0" fill="none" stroke="#fff" stroke-width="1.4"/></svg>
      Send Us an Email
    </span>
    <span class="util-item call">
      <svg width="12" height="12" viewBox="0 0 24 24"><path d="M6.6 10.8a15 15 0 0 0 6.6 6.6l2.2-2.2a1 1 0 0 1 1-.25 11.4 11.4 0 0 0 3.6.57 1 1 0 0 1 1 1V20a1 1 0 0 1-1 1A17 17 0 0 1 3 4a1 1 0 0 1 1-1h3.5a1 1 0 0 1 1 1c0 1.25.2 2.45.57 3.57a1 1 0 0 1-.25 1z" fill="#f78f20"/></svg>
      <span>Call us:<br><b>(0400 555-0199)</b></span>
    </span>
  </div>
  <nav class="main-nav">
    <a class="is-active">HOME</a>
    <a>WELCOME</a>
    <a>ABOUT</a>
    <a>SERVICES</a>
    <a style="padding-left:30px">BLOG</a>
    <a>NEWS</a>
  </nav>
</header>

<section class="hero">
  <div class="hero-photo" role="img" aria-label="Woman doing a push-up on a sunlit forest path"></div>
  <svg class="hero-arrow" style="left:46px" viewBox="0 0 40 80"><path d="M34 4 L6 40 L34 76" fill="none" stroke="#fff" stroke-width="5"/></svg>
  <svg class="hero-arrow" style="left:1090px" viewBox="0 0 40 80"><path d="M6 4 L34 40 L6 76" fill="none" stroke="#fff" stroke-width="5"/></svg>

  <form class="appointment">
    <h2>Request an<br>Appointment</h2>
    <div class="field" style="top:123px">
      <svg viewBox="0 0 20 20"><circle cx="10" cy="6" r="4.5" fill="#fff"/><path d="M2 19c0-5 3.5-7.5 8-7.5s8 2.5 8 7.5z" fill="#fff"/></svg>
      <span>Name</span>
    </div>
    <div class="field" style="top:169px">
      <svg viewBox="0 0 20 20"><rect x="2" y="4" width="16" height="14" fill="#fff"/><rect x="2" y="4" width="16" height="4" fill="#e8f3c6"/><rect x="5" y="1" width="2" height="5" fill="#fff"/><rect x="13" y="1" width="2" height="5" fill="#fff"/></svg>
      <span>Date of Birth</span>
    </div>
    <div class="field" style="top:217px">
      <svg viewBox="0 0 20 20"><rect x="1" y="4" width="18" height="12" fill="#fff"/><path d="M1 4 L10 11 L19 4" fill="none" stroke="#abd036" stroke-width="1.5"/></svg>
      <span>Email Adress</span>
    </div>
    <div class="field" style="top:264px">
      <svg viewBox="0 0 24 24"><path d="M6.6 10.8a15 15 0 0 0 6.6 6.6l2.2-2.2a1 1 0 0 1 1-.25 11.4 11.4 0 0 0 3.6.57 1 1 0 0 1 1 1V20a1 1 0 0 1-1 1A17 17 0 0 1 3 4a1 1 0 0 1 1-1h3.5a1 1 0 0 1 1 1c0 1.25.2 2.45.57 3.57a1 1 0 0 1-.25 1z" fill="#fff"/></svg>
      <span>Phone</span>
    </div>
    <div class="field" style="top:310px">
      <svg viewBox="0 0 20 20"><rect x="2" y="8" width="16" height="4" fill="#fff"/></svg>
      <span>Practice size<i class="caret"><svg width="10" height="8" viewBox="0 0 10 8"><path d="M0 0 H10 L5 7z" fill="#9a9a9a"/></svg></i></span>
    </div>
    <div class="submit-row">
      <svg width="26" height="22" viewBox="0 0 26 22"><path d="M2 2 L11 11 L2 20 M13 2 L22 11 L13 20" fill="none" stroke="#fff" stroke-width="3.5"/></svg>
      <span class="submit-btn">SUBMIT</span>
      <svg width="26" height="22" viewBox="0 0 26 22"><path d="M24 2 L15 11 L24 20 M13 2 L4 11 L13 20" fill="none" stroke="#fff" stroke-width="3.5"/></svg>
    </div>
    <p class="appointment-note">Lorem ipsum dolor sit amet<br>consectetur adipiscing elit. Sed at ante</p>
  </form>
</section>

<section class="welcome">
  <h1 class="welcome-title">WELCOME TO<br>TO OUR SITE!</h1>
  <div class="welcome-rule"></div>
  <div class="welcome-body">
    <h3>Fern Wellness &amp; Health</h3>
    <p>Lorem ipsum dolor sit amet, consectetur adipiscing elit. Sed at ante. Mauris eleifend, quam a vulputate dictum, massa quam dapibus leo, eget vulputate orci purus ut lorem. In fringilla mi in ligula. Pellentesque aliquam quam vel dolor. Nunc adipiscing.<br>Sed quam odio, tempus ac, aliquam molestie, varius ac, tellus</p>
    <span class="btn">Learn More</span>
  </div>
</section>

<section class="expertise">
  <h2 class="section-title" style="top:42px;color:var(--leaf)">Our <strong>Expertise</strong></h2>

  <div class="tile" style="left:169px;top:124px">
    <div class="photo" role="img" aria-label="Older man using an inhaler beside an exercise bike on a beach" style="background:linear-gradient(180deg,#9dc0d9 0%,#d8c9a0 55%,#8a7d55 100%)"></div>
    <span class="label">Asthma</span>
  </div>
  <div class="tile" style="left:463px;top:124px">
    <div class="photo" role="img" aria-label="Glucose meter among fresh fruit and vegetables" style="background:linear-gradient(135deg,#e9a05a 0%,#c6452d 45%,#7da33a 100%)"></div>
    <span class="label">Diabetes</span>
  </div>
  <div class="tile" style="left:760px;top:124px">
    <div class="photo" role="img" aria-label="Man doing sit-ups on a mat in a bright room" style="background:linear-gradient(180deg,#f2f2f2 0%,#dfe4ea 55%,#c4ccd6 100%)"></div>
    <span class="band"></span>
    <span class="label">Obesity</span>
  </div>
  <div class="tile" style="left:169px;top:329px">
    <div class="photo" role="img" aria-label="Group of adults exercising together outdoors" style="background:linear-gradient(180deg,#5f8a4a 0%,#3f6238 60%,#2f4a2b 100%)"></div>
    <span class="label">Rehab</span>
  </div>
  <div class="tile" style="left:463px;top:329px">
    <div class="photo" role="img" aria-label="Athlete stretching on a running track" style="background:linear-gradient(180deg,#b7cfdf 0%,#a3a26a 45%,#b0553c 100%)"></div>
    <span class="label">Sports Performance</span>
  </div>
  <div class="tile tile-more" style="left:760px;top:329px">
    <div class="photo" role="img" aria-label="Wooden deck in a green garden" style="background:linear-gradient(180deg,#6d8f4e 0%,#8aa46a 50%,#7b8c5e 100%)"></div>
    <span class="band" style="background:rgba(120,200,150,.55)"></span>
    <span class="plus"><svg width="40" height="40" viewBox="0 0 40 40"><path d="M20 4 V36 M4 20 H36" stroke="#2bb59a" stroke-width="6"/></svg></span>
  </div>
</section>

<section class="about">
  <h2 class="section-title" style="top:1562px;color:var(--amber)">About <strong>Practice</strong></h2>
  <div class="about-photo" role="img" aria-label="Japanese style garden with trees and lanterns" style="background:linear-gradient(135deg,#4f5a32 0%,#7b5a3c 45%,#9b6a5a 100%)"></div>
  <div class="about-text">
    <p>Fern Wellness &amp; Health is a private home studio built for people who need more care than a busy gym can give. Every client is screened and assessed before training begins, and each programme is shaped around a real condition, whether that is asthma, diabetes, excess weight or recovery from injury. Sessions run indoors and outdoors in all weather, so the body learns to work in the elements instead of a cold room full of machines.</p>
    <p>Work is done alongside each client's doctor, physiotherapist or allied health team so progress is safe, measured and lasting. Groups stay small because there is only one trainer, which means every person is seen, corrected and encouraged throughout the hour.</p>
    <p>Small Pilates classes are also held in a quiet Japanese garden at the back of the house. The studio is a private facility, so please ring ahead to book an appointment before visiting. Healthy food guidance is part of every plan, helping long term clients reach real goals rather than quick fixes.</p>
  </div>
  <div class="thumb" style="left:438px" role="img" aria-label="Indoor studio with wooden floor" style="background:#a07a52"></div>
  <div class="thumb" style="left:586px;background:linear-gradient(180deg,#7aa14e,#4f7a36)" role="img" aria-label="Outdoor group training on grass"></div>
  <div class="thumb" style="left:736px;background:linear-gradient(180deg,#e6e8ea,#b9c0c8)" role="img" aria-label="Light training room with equipment"></div>
  <div class="thumb" style="left:884px;background:linear-gradient(180deg,#c9d2d9,#6c7f95)" role="img" aria-label="People doing floor exercises"></div>
</section>

<style>.about .thumb:nth-of-type(1){background:linear-gradient(180deg,#b48a5f,#7a5a3a)}</style>

<section class="updates">
  <h2 class="col-title" style="left:165px;top:70px">LATEST <strong>NEWS</strong></h2>
  <h2 class="col-title" style="left:675px;top:70px">OUR <strong>BLOG</strong></h2>
  <div class="updates-rule" style="top:91px"></div>
</section>
<div class="news-photo" role="img" aria-label="Couple stretching together on a lawn" style="background:linear-gradient(180deg,#c5b98a 0%,#7c9a4c 55%,#5e8036 100%)"></div>
<div class="news-rule"></div>
<p class="news-text">Lorem ipsum dolor sit amet, consectetur adipiscing elit. Maecenas bibendum elit at eros gravida at consequat velit auctor. Curabitur vel libero eget turpis ullamcorper pereh malesuada eu sem.</p>
<span class="btn small-btn" style="left:165px;top:2390px">Read More</span>

<div class="post-thumb" style="top:2161px;background:linear-gradient(180deg,#8fa7bf,#4e5d6e)" role="img" aria-label="Blog author portrait"></div>
<div class="post" style="top:2160px">
  <time>26 DEC, 2014</time>
  Lorem ipsum dolor sit amet, consectetur adipiscing elit. Maecenas bibendum elit at eros gravida at consequat velit auctor. Curabitur vel libero eget turpis ullamcorper pereh malesuada eu sem. Sed pretium
  <span class="read-more" style="top:82px">Read More &raquo;</span>
</div>
<div class="post-thumb" style="top:2273px;background:linear-gradient(180deg,#8fa7bf,#4e5d6e)" role="img" aria-label="Blog author portrait"></div>
<div class="post" style="top:2272px">
  <time>26 DEC, 2014</time>
  Lorem ipsum dolor sit amet, consectetur adipiscing elit. Maecenas bibendum elit at eros gravida at consequat velit auctor. Curabitur vel libero eget turpis ullamcorper pereh malesuada eu sem. Sed pretium
  <span class="read-more" style="top:82px">Read More &raquo;</span>
</div>
<span class="btn small-btn" style="left:675px;top:2386px">View More</span>

<section class="testimonials">
  <h2 class="testimonials-title">TESTIMONIALS</h2>
  <p class="testimonials-sub">Lorem ipsum dolor sit amet, consectetur adipiscing elit</p>
  <svg class="t-arrow" style="left:157px" viewBox="0 0 24 44"><path d="M21 2 L3 22 L21 42" fill="none" stroke="#222" stroke-width="2.5"/></svg>
  <svg class="t-arrow" style="left:1019px" viewBox="0 0 24 44"><path d="M3 2 L21 22 L3 42" fill="none" stroke="#222" stroke-width="2.5"/></svg>

  <blockquote class="quote" style="left:245px">Training here changed how I manage my asthma. Every session was planned around my breathing, and I now walk, climb and play with my kids without fear. The garden sessions are calm, personal and genuinely enjoyable.</blockquote>
  <blockquote class="quote" style="left:617px">After knee surgery I was nervous to move again. Careful testing, patient coaching and work with my physio got me back to running. It never felt like a gym, just steady progress in a friendly, natural place.</blockquote>

  <div class="avatar" style="left:245px;background:linear-gradient(180deg,#7f8fa0,#3e4a56)" role="img" aria-label="Client portrait"></div>
  <p class="person" style="left:304px">Mr. Tom Reed<small>Client</small></p>
  <div class="avatar" style="left:617px;background:linear-gradient(180deg,#6b6b6b,#2a2a2a)" role="img" aria-label="Client portrait"></div>
  <p class="person" style="left:686px">Miss. Nora Lane<small>Client</small></p>
</section>

<footer class="site-footer">
  <h4 class="foot-title" style="left:38px">QUICK LINKS</h4>
  <ul class="quick-links">
    <li>HOME</li><li>WELCOME</li><li>SERVICES</li><li>ABOUT</li><li>NEWS</li><li>BLOG</li>
  </ul>

  <h4 class="foot-title" style="left:338px">CONTACT INFO</h4>
  <div class="contact-info">
    <svg class="pin" width="16" height="22" viewBox="0 0 16 22"><path d="M8 0a8 8 0 0 0-8 8c0 6 8 14 8 14s8-8 8-14a8 8 0 0 0-8-8z" fill="#fff"/><circle cx="8" cy="8" r="3" fill="#363636"/></svg>
    42 Willow Lane PO Box<br>208 Brookvale<br>Co 2100
    <div class="lines">Tel :+61 2 5550 1842<br>Fax :+61 2 5550 1843<br>email :hello@fernwellness.example</div>
  </div>

  <h4 class="foot-title" style="left:628px">CONTACT US</h4>
  <span class="foot-input" style="left:628px;top:91px;width:102px">First Name</span>
  <span class="foot-input" style="left:745px;top:91px;width:99px">Last Name</span>
  <span class="foot-input" style="left:628px;top:135px;width:216px">Your Email</span>
  <span class="foot-submit">SUBMIT</span>

  <div class="foot-brand">
    <span class="brand-dot"></span>
    <span class="brand-name">Fern Wellness &amp; Health</span>
  </div>
  <div class="social"><span></span><span></span><span></span></div>
</footer>
<div class="copyright">copyright 2014 yourname</div>

</body>
</html>
```